Tobin Quartz Portal Page . It's guarantee project!

We need a clean and professional modern web application portal page
That includes the Login & Application Selection screen

Also, I need to design both Desktop and Mobile sizes.
We have an example design for our target

The application is Jetty Schedule and related data.
Our client is a bit conservative.

Theme color preferred : #00508B (main) #DF0D83 (secondary)

Target Market(s)

Oil & Fuel & Gasoline

Number of Pages Required

2 page

Font styles to use
Sans Serif

Colors
0054AA
0677BA
7BADD7
CADEEF
E8F1F8
E54698
E96AAD
F1A4CE
F9D9EA
FCEFF6

Requirements
Must have
• Login Page & Main Screen

```html
<!DOCTYPE html>
<html lang="en">
<head>
<meta charset="utf-8">
<title>Tobin Quartz Portal – Sign In &amp; Application Selection</title>
<link rel="stylesheet" href="https://fonts.googleapis.com/css2?family=Inter:wght@400;500;600;700&display=swap">
<style>
  :root{
    --board:#EFEBEB;
    --frame-edge:#D9D6D6;
    --white:#FFFFFF;
    --header:#DFEFF7;
    --ink:#00508B;
    --ink-deep:#0B3F6E;
    --field-edge:#0677BA;
    --accent:#DF0D83;
    --illus-a:#E8E6FB;
    --illus-b:#7BADD7;
    --illus-c:#F1A4CE;
    --card-shadow:rgba(0,80,139,0.10);
  }
  *{box-sizing:border-box;margin:0;padding:0}
  html,body{width:1200px;height:923px;overflow:hidden;background:var(--board)}
  body{font-family:"Inter",sans-serif;color:var(--ink);position:relative}

  .board-label{position:absolute;font-size:10px;font-weight:500;color:var(--ink)}

  .screen{position:absolute;background:var(--white);border:1px solid var(--frame-edge);overflow:hidden}
  .topbar{position:absolute;left:0;top:0;width:100%;background:var(--header)}

  .brand{position:absolute;display:flex;align-items:center;gap:3px;font-size:7.5px;font-weight:600;color:var(--ink)}
  .brand-dot{width:9px;height:9px;border-radius:50%;background:var(--accent)}

  .signin-title{position:absolute;left:0;width:100%;text-align:center;font-size:9.5px;font-weight:600;color:var(--ink);transform:translateY(-50%)}
  .field{position:absolute;height:21px;border:0.7px solid var(--field-edge);border-radius:2px}
  .field-label{position:absolute;left:5px;top:-3.5px;padding:0 1.5px;background:var(--white);font-size:5.2px;color:var(--ink-deep);line-height:6px}
  .field-eye{position:absolute;right:5px;top:50%;transform:translateY(-50%);width:8px;height:8px}
  .primary-btn{position:absolute;height:21.5px;border-radius:1.5px;background:var(--accent);color:var(--white);font-size:5.5px;font-weight:500;display:flex;align-items:center;justify-content:center;letter-spacing:.1px}

  .home-link{position:absolute;display:flex;align-items:center;gap:2px;font-size:6px;color:var(--ink);transform:translateY(-50%)}
  .home-link svg{width:6px;height:6px}
  .home-icon-only{position:absolute;width:10px;height:10px;transform:translateY(-50%)}
  .user{position:absolute;line-height:1.25}
  .user-name{font-size:6.2px;font-weight:600;color:var(--ink-deep)}
  .user-mail{font-size:5.2px;color:var(--ink)}
  .avatar{position:absolute;width:14px;height:14px;border-radius:50%;background:var(--white);transform:translate(-50%,-50%);display:flex;align-items:center;justify-content:center}
  .avatar svg{width:8px;height:8px}

  .app-card{position:absolute;background:var(--white);border-radius:9px;box-shadow:0 1px 4px var(--card-shadow),0 0 0 0.6px rgba(0,80,139,0.06)}
  .app-art{position:absolute;left:50%;transform:translateX(-50%);border-radius:48%;background:radial-gradient(circle at 40% 35%,var(--illus-a) 0%,var(--illus-b) 70%,var(--illus-c) 100%)}
  .app-name{position:absolute;left:0;width:100%;text-align:center;font-weight:600;color:var(--ink);transform:translateY(-50%);white-space:nowrap}
  .app-card.lg .app-name{font-size:8.5px}
  .app-card.sm .app-name{font-size:6.2px}
</style>
</head>
<body>

<!-- Board labels -->
<div class="board-label" style="left:17.6px;top:18px">Desktop 1440</div>
<div class="board-label" style="left:616.5px;top:18px">Desktop 1440</div>
<div class="board-label" style="left:17.6px;top:484px">Tablet 768</div>
<div class="board-label" style="left:341px;top:484px">Mobile 375</div>
<div class="board-label" style="left:616.5px;top:484px">Tablet 768</div>
<div class="board-label" style="left:940px;top:484px">Mobile 375</div>

<!-- Desktop sign in -->
<section class="screen" style="left:17.6px;top:39px;width:559.5px;height:398.6px">
  <header class="topbar" style="height:31px">
    <div class="brand" style="left:57px;top:10px"><span class="brand-dot"></span>Tobin Quartz</div>
  </header>
  <h1 class="signin-title" style="top:67px">SIGN IN</h1>
  <div class="field" style="left:209.4px;top:89.5px;width:140px"><span class="field-label">Email</span></div>
  <div class="field" style="left:209.4px;top:123.5px;width:140px"><span class="field-label">Password</span>
    <svg class="field-eye" viewBox="0 0 24 24" fill="none" stroke="#0B3F6E" stroke-width="2.4" stroke-linecap="round"><path d="M2 12s4-7 10-7 10 7 10 7-4 7-10 7S2 12 2 12z"/><circle cx="12" cy="12" r="3"/><path d="M3 3l18 18"/></svg>
  </div>
  <div class="primary-btn" style="left:209.4px;top:164px;width:140px">SIGN IN</div>
</section>

<!-- Desktop application selection -->
<section class="screen" style="left:616.5px;top:39px;width:559.5px;height:398.6px">
  <header class="topbar" style="height:31px">
    <div class="home-link" style="left:58.5px;top:16px"><svg viewBox="0 0 24 24" fill="none" stroke="#00508B" stroke-width="2.2"><path d="M3 11l9-8 9 8v10H3z"/><path d="M9 21v-6h6v6"/></svg>Home</div>
    <div class="user" style="left:419.5px;top:8px"><div class="user-name">Mara Lind</div><div class="user-mail">mara.lind@example.com</div></div>
    <div class="avatar" style="left:493.5px;top:15.5px"><svg viewBox="0 0 24 24" fill="#0B3F6E"><circle cx="12" cy="8" r="5"/><path d="M3 22c0-5 4-8 9-8s9 3 9 8z"/></svg></div>
  </header>
  <div class="app-card lg" style="left:58.5px;top:56px;width:141px;height:141px">
    <div class="app-art" role="img" aria-label="Illustration of a clock, calendar, envelope and checklist for planning" style="top:18px;width:100px;height:86px"></div>
    <div class="app-name" style="top:124px">Jetty Planning</div>
  </div>
  <div class="app-card lg" style="left:209.2px;top:56px;width:141px;height:141px">
    <div class="app-art" role="img" aria-label="Illustration of a route map, location pins, ship and phone for tracking" style="top:18px;width:100px;height:86px"></div>
    <div class="app-name" style="top:124px">Jetty Tracking</div>
  </div>
  <div class="app-card lg" style="left:360.2px;top:56px;width:141px;height:141px">
    <div class="app-art" role="img" aria-label="Illustration of an oil rig, cargo ships and a target for port performance" style="top:18px;width:100px;height:86px"></div>
    <div class="app-name" style="top:124px">Jetty/Port Perfomance</div>
  </div>
</section>

<!-- Tablet sign in -->
<section class="screen" style="left:17.6px;top:505.6px;width:298px;height:398px">
  <header class="topbar" style="height:24.7px">
    <div class="brand" style="left:12px;top:8px"><span class="brand-dot"></span>Tobin Quartz</div>
  </header>
  <h1 class="signin-title" style="top:61px">SIGN IN</h1>
  <div class="field" style="left:79px;top:83.4px;width:139.6px"><span class="field-label">Email</span></div>
  <div class="field" style="left:79px;top:117.4px;width:139.6px"><span class="field-label">Password</span>
    <svg class="field-eye" viewBox="0 0 24 24" fill="none" stroke="#0B3F6E" stroke-width="2.4" stroke-linecap="round"><path d="M2 12s4-7 10-7 10 7 10 7-4 7-10 7S2 12 2 12z"/><circle cx="12" cy="12" r="3"/><path d="M3 3l18 18"/></svg>
  </div>
  <div class="primary-btn" style="left:79px;top:158.4px;width:139.6px">SIGN IN</div>
</section>

<!-- Mobile sign in -->
<section class="screen" style="left:341px;top:505.6px;width:145.5px;height:259px">
  <header class="topbar" style="height:24.7px">
    <div class="brand" style="left:6px;top:8px"><span class="brand-dot"></span>Tobin Quartz</div>
  </header>
  <h1 class="signin-title" style="top:61px">SIGN IN</h1>
  <div class="field" style="left:6px;top:83.4px;width:133px"><span class="field-label">Email</span></div>
  <div class="field" style="left:6px;top:117.4px;width:133px"><span class="field-label">Password</span>
    <svg class="field-eye" viewBox="0 0 24 24" fill="none" stroke="#0B3F6E" stroke-width="2.4" stroke-linecap="round"><path d="M2 12s4-7 10-7 10 7 10 7-4 7-10 7S2 12 2 12z"/><circle cx="12" cy="12" r="3"/><path d="M3 3l18 18"/></svg>
  </div>
  <div class="primary-btn" style="left:6px;top:158.4px;width:133px">SIGN IN</div>
</section>

<!-- Tablet application selection -->
<section class="screen" style="left:616.5px;top:505.6px;width:298px;height:398px">
  <header class="topbar" style="height:24.7px">
    <div class="home-link" style="left:12.5px;top:12.5px"><svg viewBox="0 0 24 24" fill="none" stroke="#00508B" stroke-width="2.2"><path d="M3 11l9-8 9 8v10H3z"/><path d="M9 21v-6h6v6"/></svg>Home</div>
    <div class="user" style="left:204px;top:5px"><div class="user-name">Mara Lind</div><div class="user-mail">mara.lind@example.com</div></div>
    <div class="avatar" style="left:278.5px;top:12.5px"><svg viewBox="0 0 24 24" fill="#0B3F6E"><circle cx="12" cy="8" r="5"/><path d="M3 22c0-5 4-8 9-8s9 3 9 8z"/></svg></div>
  </header>
  <div class="app-card sm" style="left:14.5px;top:50px;width:83.5px;height:83.5px">
    <div class="app-art" role="img" aria-label="Illustration of a clock, calendar, envelope and checklist for planning" style="top:9px;width:64px;height:57px"></div>
    <div class="app-name" style="top:74.5px">Jetty Planning</div>
  </div>
  <div class="app-card sm" style="left:107.5px;top:50px;width:83.5px;height:83.5px">
    <div class="app-art" role="img" aria-label="Illustration of a route map, location pins, ship and phone for tracking" style="top:9px;width:64px;height:57px"></div>
    <div class="app-name" style="top:74.5px">Jetty Tracking</div>
  </div>
  <div class="app-card sm" style="left:201px;top:50px;width:83.5px;height:83.5px">
    <div class="app-art" role="img" aria-label="Illustration of an oil rig, cargo ships and a target for port performance" style="top:9px;width:64px;height:57px"></div>
    <div class="app-name" style="top:74.5px">Jetty/Port Perfomance</div>
  </div>
</section>

<!-- Mobile application selection -->
<section class="screen" style="left:940px;top:505.6px;width:145.5px;height:320px">
  <header class="topbar" style="height:24.7px">
    <svg class="home-icon-only" style="left:7px;top:12.5px" viewBox="0 0 24 24" fill="none" stroke="#00508B" stroke-width="2"><path d="M3 11l9-8 9 8v10H3z"/><path d="M9 21v-6h6v6"/></svg>
    <div class="user" style="left:57.5px;top:5px"><div class="user-name">Mara Lind</div><div class="user-mail">mara.lind@example.com</div></div>
    <div class="avatar" style="left:131.6px;top:12.5px"><svg viewBox="0 0 24 24" fill="#0B3F6E"><circle cx="12" cy="8" r="5"/><path d="M3 22c0-5 4-8 9-8s9 3 9 8z"/></svg></div>
  </header>
  <div class="app-card sm" style="left:31px;top:38px;width:83px;height:83.5px">
    <div class="app-art" role="img" aria-label="Illustration of a clock, calendar, envelope and checklist for planning" style="top:8px;width:64px;height:57px"></div>
    <div class="app-name" style="top:74.5px">Jetty Planning</div>
  </div>
  <div class="app-card sm" style="left:31px;top:131.4px;width:83px;height:83.5px">
    <div class="app-art" role="img" aria-label="Illustration of a route map, location pins, ship and phone for tracking" style="top:8px;width:64px;height:57px"></div>
    <div class="app-name" style="top:74.5px">Jetty Tracking</div>
  </div>
  <div class="app-card sm" style="left:31px;top:224.4px;width:83px;height:83.5px">
    <div class="app-art" role="img" aria-label="Illustration of an oil rig, cargo ships and a target for port performance" style="top:8px;width:64px;height:57px"></div>
    <div class="app-name" style="top:74.5px">Jetty/Port Perfomance</div>
  </div>
</section>

</body>
</html>
```